Awesome Business Card Design needed!

Hey there.
I'm looking for a simple but awesome business card design.
Type of company: Online advertisement agency
(please don't use the typical business people or statistics images on the card)
The front has to display the business name
and possibly some sort of logo ( perhaps something with the two M's of the biz name )
And the back of the card should say:
Name
Phone
Email
Let your imagination flow.
here are some designs that I like and that you can use as inspiration.
Simple but Awesome
http://images.pixelvantor.net/designs/55128_877673_43091_thumbnail.jpg
http://images.pixelvantor.net/designs/37714_747642_40106_image.jpg
http://images.pixelvantor.net/designs/55128_877673_43091_image.jpg
http://images.pixelvantor.net/designs/51321_781878_43091_image.jpg
http://images.pixelvantor.net/designs/33378_399063_15912_image.jpg
http://images.pixelvantor.net/designs/2337_271604_9495_image.jpg
good luck

```html
<!DOCTYPE html>
<html lang="en">
<head>
<meta charset="utf-8">
<title>Vardello Media – Business Cards</title>
<link rel="stylesheet" href="https://fonts.googleapis.com/css2?family=Archivo:wght@400;700&display=swap">
<style>
  :root {
    --page-bg: #3a3a3a;
    --card-edge: #0c0f10;
    --card-center: #2a3233;
    --card-dark: #121617;
    --ink-light: #d9dcdd;
    --ink-muted: #a9aeb0;
    --accent-blue: #4a9ee0;
    --rule: #5a6163;
  }
  * { box-sizing: border-box; margin: 0; padding: 0; }
  html, body {
    width: 1200px;
    height: 880px;
    overflow: hidden;
  }
  body {
    background: var(--page-bg);
    font-family: "Archivo", Arial, sans-serif;
    display: flex;
    align-items: center;
    justify-content: center;
    gap: 60px;
  }
  .card {
    width: 520px;
    height: 300px;
    border-radius: 4px;
    background: radial-gradient(ellipse at 50% 40%, var(--card-center) 0%, var(--card-dark) 60%, var(--card-edge) 100%);
    box-shadow: 0 14px 30px rgba(0,0,0,0.45);
    display: flex;
    flex-direction: column;
    align-items: center;
    justify-content: center;
    color: var(--ink-light);
    text-transform: uppercase;
  }
  .brand {
    display: flex;
    flex-direction: column;
    align-items: center;
    gap: 18px;
  }
  .brand-square {
    width: 64px;
    height: 64px;
    background: var(--accent-blue);
  }
  .brand-name {
    font-weight: 700;
    font-size: 30px;
    letter-spacing: 0.5px;
    color: var(--ink-light);
  }
  .card-back .brand-square { width: 48px; height: 48px; }
  .card-back .brand-name { font-size: 22px; }
  .contact {
    margin-top: 22px;
    display: flex;
    flex-direction: column;
    align-items: center;
  }
  .contact-name {
    font-weight: 700;
    font-size: 19px;
    letter-spacing: 0.5px;
    padding-bottom: 8px;
    border-bottom: 1px solid var(--rule);
    margin-bottom: 10px;
  }
  .contact-line {
    font-size: 14px;
    letter-spacing: 0.5px;
    color: var(--ink-muted);
    line-height: 1.6;
  }
  .contact-line .label { color: var(--ink-light); font-weight: 700; }
</style>
</head>
<body>
  <section class="card card-front" aria-label="Card front">
    <div class="brand">
      <span class="brand-square" aria-hidden="true"></span>
      <span class="brand-name">Vardello Media</span>
    </div>
  </section>

  <section class="card card-back" aria-label="Card back">
    <div class="brand">
      <span class="brand-square" aria-hidden="true"></span>
      <span class="brand-name">Vardello Media</span>
    </div>
    <div class="contact">
      <p class="contact-name">Daniel Whitaker</p>
      <p class="contact-line"><span class="label">P:</span> 1555 014 2293</p>
      <p class="contact-line"><span class="label">E:</span> info@vardellomedia.com</p>
    </div>
  </section>
</body>
</html>
```